Business Card Design Project

We are a distribution company providing goods to Latin America. We sell everything from Medical equipment, generic medicines, to carecliners. The logo that we use is attached. The logo can incorporate different colors other than black for versatility. The company name is Valdren Global Enterprises and/or VGE. The card will be printed using 1 or more of the following: Silk mounted and/or embossed. So if the design ideas could be made to incorporate that technique or any other unique techniques, it would be great. The target market is dialysis centers/doctors.

Basic Info for card:
Marna Dowell
Purchasing Manager
417-305-6184 direct
417-521-7790 fax
marna.dowell@valdrenvge.example
www.valdrenvge.example

Target Market(s)

Latin America

Industry/Entity Type

Business

Requirements
Nice to have
• The Front of the card should have the basic contact information with company name/logo. The back of the card could incorporate

```html
<!DOCTYPE html>
<html lang="en">
<head>
<meta charset="utf-8">
<title>Valdren Global Enterprises — Business Card</title>
<link rel="stylesheet" href="https://fonts.googleapis.com/css2?family=Marcellus&family=Tinos:wght@700&display=swap">
<style>
  :root {
    --ink: #000000;
    --paper: #ffffff;
    --brand-blue: #1f5ef2;
    --card-black: #000000;
    --card-edge: #8a8a8a;
    --label-font: "Tinos", "Times New Roman", serif;
    --card-font: "Marcellus", Georgia, serif;
  }
  html, body {
    margin: 0;
    padding: 0;
    width: 893px;
    height: 1200px;
    overflow: hidden;
    background: var(--paper);
  }
  .sheet {
    position: relative;
    width: 893px;
    height: 1200px;
    font-family: var(--card-font);
    color: var(--ink);
  }
  .side-label {
    position: absolute;
    left: 0;
    width: 100%;
    text-align: center;
    font-family: var(--label-font);
    font-weight: 700;
    font-size: 50px;
    line-height: 1;
    margin: 0;
  }
  .side-label--front { top: 2px; }
  .side-label--back { top: 1153px; }

  .card {
    position: absolute;
    left: 1px;
    width: 889px;
    height: 523px;
    box-sizing: border-box;
  }
  .card--front {
    top: 58px;
    background: var(--card-black);
    border: 1px solid var(--card-edge);
  }
  .card--back {
    top: 610px;
    background: var(--paper);
    border: 1.5px solid var(--ink);
  }

  /* front */
  .brand-name {
    position: absolute;
    left: 0;
    width: 100%;
    top: 215px;
    text-align: center;
    font-size: 50px;
    line-height: 1;
    color: var(--brand-blue);
  }
  .brand-initials {
    position: absolute;
    left: 0;
    width: 100%;
    top: 458px;
    text-align: center;
    font-size: 34px;
    letter-spacing: 4px;
    line-height: 1;
    color: var(--brand-blue);
  }

  /* back */
  .card--back .centered {
    position: absolute;
    left: 0;
    width: 100%;
    text-align: center;
    margin: 0;
  }
  .holder-name {
    top: 78px;
    font-size: 70px;
    line-height: 1;
  }
  .name-rule {
    position: absolute;
    left: 83px;
    width: 709px;
    top: 148px;
    height: 0;
    border-top: 1.5px solid var(--brand-blue);
  }
  .holder-title {
    top: 164px;
    font-size: 33px;
    line-height: 1;
  }
  .contact-list {
    top: 283px;
    list-style: none;
    padding: 0;
    font-size: 24px;
    line-height: 34.5px;
  }
  .contact-list .tag { font-size: 19px; }
  .contact-list .small { font-size: 21px; }
  .company-name {
    top: 438px;
    font-size: 48px;
    line-height: 1;
    color: var(--brand-blue);
  }
</style>
</head>
<body>
<main class="sheet">
  <h2 class="side-label side-label--front">FRONT</h2>

  <section class="card card--front" aria-label="Card front">
    <div class="brand-name">Valdren Global Enterprises</div>
    <div class="brand-initials">VGE</div>
  </section>

  <section class="card card--back" aria-label="Card back">
    <h1 class="centered holder-name">Marna Dowell</h1>
    <div class="name-rule"></div>
    <p class="centered holder-title">Purchasing Manager</p>
    <ul class="centered contact-list">
      <li>417-305-6184 <span class="tag">direct</span></li>
      <li>417-521-7790 <span class="tag">fax</span></li>
      <li class="small">marna.dowell@valdrenvge.example</li>
      <li class="small">www.valdrenvge.example</li>
    </ul>
    <p class="centered company-name">Valdren Global Enterprises</p>
  </section>

  <h2 class="side-label side-label--back">BACK</h2>
</main>
</body>
</html>
```